Skin care manufacturer looking for packaging design for new skin care brand.

We need a design and logo for a skin care brand to be sold at retail stores and online in the United States and Europe. The design will be for 1.7oz - 2oz serums that will not have a retail box. The name of the brand is Clear Meadow and should be a luxurious brand that is approachable. The brand will consist of 4 face serums - Vitamin C, Collagen, Retinol and Hyaluronic Acid. Images shown are for inspiration only. Color of bottles can be varied based on design and bottles can be screen printed or labeled.

Need extra days to review

Target Market(s)

Target market is 30+ female

Industry/Entity Type

Beauty

Requirements
Must have
• Ingredient call outs + benefit. Ex: Vitamin C Brightening Serum. Packaging should be translucent

```html
<!DOCTYPE html>
<html lang="en">
<head>
<meta charset="UTF-8">
<title>Clear Meadow Serum Collection</title>
<link rel="stylesheet" href="https://fonts.googleapis.com/css2?family=Josefin+Sans:wght@400&family=Cormorant+Garamond:wght@500&family=Lora:wght@400;700&display=swap">
<style>
  :root {
    --backdrop: #e6e6e6;
    --vitamin: #e9836a;
    --hyaluronic: #22bde6;
    --collagen: #7479cc;
    --retinol: #d93e8c;
    --dropper: #f4f4f4;
    --cap-light: #f2f2f2;
    --cap-dark: #8d8d8d;
    --label-white: #ffffff;
    --ink: #1c1c1c;
  }
  * { margin: 0; padding: 0; box-sizing: border-box; }
  html, body { width: 1200px; height: 900px; overflow: hidden; }
  body { background: var(--backdrop); position: relative; }

  .collection { position: absolute; inset: 0; }
  .bottle {
    position: absolute; top: 87px; width: 240px; height: 684px;
    margin-left: -120px; text-align: center;
  }
  .bottle svg { position: absolute; inset: 0; width: 240px; height: 684px; }
  .bottle--vitamin { left: 208px; color: var(--vitamin); }
  .bottle--hyaluronic { left: 482px; color: var(--hyaluronic); }
  .bottle--collagen { left: 749px; color: var(--collagen); }
  .bottle--retinol { left: 1018px; color: var(--retinol); }

  .brand-name {
    position: absolute; top: 346px; left: 0; right: 0;
    font-family: "Josefin Sans", sans-serif; font-size: 21px;
    letter-spacing: 1px; color: var(--label-white);
  }
  .ingredient {
    position: absolute; top: 436px; left: -10px; right: -10px;
    font-family: "Cormorant Garamond", serif; font-weight: 500;
    font-size: 27px; color: var(--label-white); letter-spacing: 0.3px;
  }
  .bottle--hyaluronic .ingredient { font-size: 24px; top: 438px; }
  .benefit-tag {
    position: absolute; top: 468px; left: 50%; transform: translateX(-50%);
    background: var(--label-white); color: var(--ink);
    font-family: "Lora", serif; font-weight: 700; font-size: 9px;
    letter-spacing: 0.8px; padding: 2px 6px; white-space: nowrap; min-width: 122px;
  }
  .description {
    position: absolute; top: 529px; left: 0; right: 0;
    font-family: "Lora", serif; font-size: 10px; line-height: 13px;
    color: rgba(255,255,255,0.82); letter-spacing: 0.3px;
  }
  .volume-band {
    position: absolute; top: 614px; left: 4px; right: 4px; height: 12px;
    background: linear-gradient(90deg, #cfd3d6, #ffffff 50%, #cfd3d6);
    font-family: "Lora", serif; font-weight: 700; font-size: 7px;
    line-height: 12px; color: var(--ink); letter-spacing: 0.3px;
  }
</style>
</head>
<body>
<svg width="0" height="0" style="position:absolute">
  <defs>
    <linearGradient id="cap-metal" x1="0" x2="1">
      <stop offset="0" stop-color="#7d7d7d"/>
      <stop offset="0.2" stop-color="#f5f5f5"/>
      <stop offset="0.45" stop-color="#9a9a9a"/>
      <stop offset="0.7" stop-color="#f0f0f0"/>
      <stop offset="1" stop-color="#777"/>
    </linearGradient>
    <linearGradient id="body-shade" x1="0" x2="1">
      <stop offset="0" stop-color="#000" stop-opacity="0.12"/>
      <stop offset="0.5" stop-color="#fff" stop-opacity="0.08"/>
      <stop offset="1" stop-color="#000" stop-opacity="0.12"/>
    </linearGradient>
    <symbol id="serum-bottle" viewBox="0 0 240 684">
      <path d="M86 112 V34 a34 34 0 0 1 68 0 V112 Z" fill="var(--dropper)"/>
      <rect x="52" y="110" width="136" height="90" rx="3" fill="url(#cap-metal)"/>
      <rect x="50" y="200" width="140" height="16" rx="6" fill="currentColor"/>
      <path d="M64 214 H176 V232 C220 244 236 280 236 330 V662 a20 20 0 0 1 -20 20 H24 a20 20 0 0 1 -20 -20 V330 C4 280 20 244 64 232 Z" fill="currentColor"/>
      <path d="M64 214 H176 V232 C220 244 236 280 236 330 V662 a20 20 0 0 1 -20 20 H24 a20 20 0 0 1 -20 -20 V330 C4 280 20 244 64 232 Z" fill="url(#body-shade)"/>
    </symbol>
  </defs>
</svg>

<main class="collection">
  <article class="bottle bottle--vitamin">
    <svg><use href="#serum-bottle"/></svg>
    <p class="brand-name">CLEAR MEADOW</p>
    <h2 class="ingredient">VITAMIN C</h2>
    <p class="benefit-tag">BRIGHTENING SERUM</p>
    <p class="description">Lorem Ipsum is simply<br>dummy text of the printing<br>and typesetting industry.</p>
    <p class="volume-band">50ML/1.7 FLO OZ</p>
  </article>

  <article class="bottle bottle--hyaluronic">
    <svg><use href="#serum-bottle"/></svg>
    <p class="brand-name">CLEAR MEADOW</p>
    <h2 class="ingredient">HYALURONIC ACID</h2>
    <p class="benefit-tag">FACIAL SERUM</p>
    <p class="description">Lorem Ipsum is simply<br>dummy text of the printing<br>and typesetting industry.</p>
    <p class="volume-band">50ML/1.7 FLO OZ</p>
  </article>

  <article class="bottle bottle--collagen">
    <svg><use href="#serum-bottle"/></svg>
    <p class="brand-name">CLEAR MEADOW</p>
    <h2 class="ingredient">COLLAGEN</h2>
    <p class="benefit-tag">BRIGHTENING SERUM</p>
    <p class="description">Lorem Ipsum is simply<br>dummy text of the printing<br>and typesetting industry.</p>
    <p class="volume-band">50ML/1.7 FLO OZ</p>
  </article>

  <article class="bottle bottle--retinol">
    <svg><use href="#serum-bottle"/></svg>
    <p class="brand-name">CLEAR MEADOW</p>
    <h2 class="ingredient">RETINOL</h2>
    <p class="benefit-tag">BRIGHTENING SERUM</p>
    <p class="description">Lorem Ipsum is simply<br>dummy text of the printing<br>and typesetting industry.</p>
    <p class="volume-band">50ML/1.7 FLO OZ</p>
  </article>
</main>
</body>
</html>
```